2012 Calendar Design

This calendar will be a Ironpulse themed calendar (http://games.ironpulse-example.com/) for more about ironpulse. It is fitness related and should graphically relate to the ironpulse style as seen on the website. Darker, a bit grungy is good...

Calendar to 8.5 x 11 designed in adobe indesign and completely editable, allowing for updates and changes to the images, calendar, dates. Detail specs are as follows;

Width = 8.25 in / Height = 10.75
Margins: Top = 0.25 in / Bottom = 0.25 in / Inside = 0.25 in / Outside = 0.25 in
Bleeds: Top = 0.125 in / Bottom = 0.125 in / Inside = 0 in / Outside = 0.25 in

See here for example of final layout;

http://www.printnook-example.com/browse/issue/730562

I will provide image files for each page.

Target Market(s)

Ironpulse Athelets, Gym Owners, Sports and Nutrition

Industry/Entity Type

Fitness

Requirements
Must have
• Designed in Adobe Indesign and fully editable

```html
<!DOCTYPE html>
<html lang="en">
<head>
<meta charset="utf-8">
<title>Ironpulse 2012 Calendar – February</title>
<link rel="stylesheet" href="https://fonts.googleapis.com/css2?family=Anton&family=Francois+One&family=Oswald:wght@600&family=Sorts+Mill+Goudy&family=Arimo&display=swap">
<style>
  :root {
    --paper-light: #c9a979;
    --paper-mid: #a98655;
    --paper-dark: #6e4f2c;
    --photo-light: #a88a5c;
    --photo-dark: #2e2416;
    --rule: #8a3a14;
    --year-top: #d9661c;
    --year-bottom: #6a2410;
    --calendar-red: #8e2a17;
    --weekday: #9a3f14;
    --date-ink: #1c1208;
    --white: #ffffff;
    --body-text: #fbf3e4;
  }
  html, body {
    margin: 0;
    padding: 0;
    overflow: hidden;
  }
  body {
    width: 930px;
    height: 1200px;
    background: #ffffff;
  }
  .page {
    position: relative;
    width: 930px;
    height: 1200px;
    overflow: hidden;
    background:
      radial-gradient(ellipse at 55% 75%, rgba(255, 235, 190, 0.35), transparent 60%),
      radial-gradient(ellipse at 0% 100%, rgba(60, 35, 10, 0.45), transparent 45%),
      radial-gradient(ellipse at 100% 0%, rgba(60, 35, 10, 0.35), transparent 40%),
      linear-gradient(160deg, var(--paper-light), var(--paper-mid) 55%, var(--paper-dark));
    box-shadow: inset 0 0 0 14px rgba(255, 255, 255, 0.9), inset 0 0 0 16px rgba(90, 60, 30, 0.5);
  }
  .hero-photo {
    position: absolute;
    left: 15px;
    top: 68px;
    width: 897px;
    height: 602px;
    background:
      radial-gradient(ellipse at 50% 40%, var(--photo-light), transparent 70%),
      linear-gradient(180deg, #5a4a32 0%, var(--photo-dark) 45%, #7d6444 80%, #9a7c52 100%);
  }
  .header-rule {
    position: absolute;
    left: 45px;
    top: 710px;
    width: 847px;
    height: 2px;
    background: var(--rule);
  }
  .column-divider {
    position: absolute;
    left: 289px;
    top: 740px;
    width: 2px;
    height: 372px;
    background: var(--rule);
  }
  .title-year {
    position: absolute;
    left: 66px;
    top: 730px;
    margin: 0;
    font-family: "Francois One", sans-serif;
    font-size: 86px;
    line-height: 1;
    letter-spacing: 2px;
    background: linear-gradient(180deg, var(--year-top), var(--year-bottom));
    -webkit-background-clip: text;
    background-clip: text;
    color: transparent;
  }
  .title-calendar {
    position: absolute;
    left: 68px;
    top: 806px;
    margin: 0;
    font-family: "Oswald", sans-serif;
    font-weight: 600;
    font-size: 34px;
    line-height: 1;
    color: var(--calendar-red);
    letter-spacing: 0.5px;
  }
  .intro-text {
    position: absolute;
    left: 45px;
    top: 890px;
    width: 232px;
    margin: 0;
    font-family: "Arimo", sans-serif;
    font-size: 13.3px;
    line-height: 17.6px;
    text-align: justify;
    color: var(--body-text);
  }
  .month-name {
    position: absolute;
    left: 296px;
    top: 1030px;
    margin: 0;
    transform: rotate(-90deg);
    transform-origin: left top;
    font-family: "Anton", sans-serif;
    font-size: 66px;
    line-height: 1;
    color: var(--white);
    white-space: nowrap;
  }
  .month-grid {
    position: absolute;
    left: 365px;
    top: 760px;
    width: 560px;
    display: grid;
    grid-template-columns: repeat(7, 80px);
  }
  .weekday {
    text-align: center;
    font-family: "Oswald", sans-serif;
    font-weight: 600;
    font-size: 26px;
    line-height: 36px;
    height: 90px;
    color: var(--weekday);
  }
  .day {
    text-align: center;
    font-family: "Sorts Mill Goudy", serif;
    font-size: 37px;
    line-height: 48.5px;
    color: var(--date-ink);
  }
</style>
</head>
<body>
<main class="page">
  <div class="hero-photo" role="img" aria-label="Sepia photograph of a group of shirtless athletes sprinting across a sandy beach"></div>

  <div class="header-rule"></div>

  <h1 class="title-year">2012</h1>
  <h2 class="title-calendar">CALENDAR</h2>

  <p class="intro-text">Ironpulse begins with a belief in fitness. The aim of Ironpulse is to forge a broad, general, and inclusive fitness. We have sought to build a program that will best prepare trainees for any physical contingency—not only for the unknown, but for the unknowable. After looking at all sport and physical tasks collectively, we asked what physical skills and adaptations would most universally lend themselves to</p>

  <div class="column-divider"></div>

  <h3 class="month-name">February</h3>

  <section class="month-grid" aria-label="February 2012">
    <div class="weekday">S</div><div class="weekday">M</div><div class="weekday">T</div><div class="weekday">W</div><div class="weekday">T</div><div class="weekday">F</div><div class="weekday">S</div>

    <div class="day"></div><div class="day"></div><div class="day"></div><div class="day"></div><div class="day"></div><div class="day"></div><div class="day">1</div>
    <div class="day">2</div><div class="day">3</div><div class="day">4</div><div class="day">5</div><div class="day">6</div><div class="day">7</div><div class="day">8</div>
    <div class="day">9</div><div class="day">10</div><div class="day">11</div><div class="day">12</div><div class="day">13</div><div class="day">14</div><div class="day">15</div>
    <div class="day">16</div><div class="day">17</div><div class="day">18</div><div class="day">19</div><div class="day">20</div><div class="day">21</div><div class="day">22</div>
    <div class="day">23</div><div class="day">24</div><div class="day">25</div><div class="day">26</div><div class="day">27</div><div class="day">28</div><div class="day">29</div>
    <div class="day">30</div><div class="day">31</div>
  </section>
</main>
</body>
</html>
```